Korvex Systems*

Stationary design including business cards, letter heads, envelops and email signatures using our new logo

Target Market(s)

Innovative Technologies

Industry/Entity Type

Defense Contracting

Font styles to use
Sans Serif

```html
<!DOCTYPE html>
<html lang="en">
<head>
<meta charset="utf-8">
<title>Korvex Systems – Business Card</title>
<link rel="stylesheet" href="https://fonts.googleapis.com/css2?family=Roboto:wght@400;700&display=swap">
<style>
  :root {
    --page-bg: #e9e9ea;
    --card-bg: #2a2b2c;
    --card-bg-deep: #232425;
    --text-light: #ffffff;
    --text-soft: #e4e4e4;
    --divider: #8a8a8a;
    --emboss: #3a3b3c;
    --emboss-edge: #47484a;
  }
  * { box-sizing: border-box; margin: 0; padding: 0; }
  html, body {
    width: 1200px; height: 900px; overflow: hidden;
    background: var(--page-bg);
    font-family: "Roboto", sans-serif;
  }
  .sheet {
    width: 1200px; height: 900px;
    display: flex; flex-direction: column;
    align-items: center; justify-content: center; gap: 40px;
  }
  .card {
    width: 680px; height: 388px;
    background: linear-gradient(160deg, var(--card-bg) 0%, var(--card-bg-deep) 100%);
    box-shadow: 0 10px 28px rgba(0,0,0,.25);
    position: relative;
  }
  /* Front */
  .card--front { display: flex; align-items: center; }
  .brand {
    width: 330px; display: flex; align-items: center; justify-content: center; gap: 14px;
  }
  .brand__mark { width: 18px; height: 18px; background: var(--text-light); }
  .brand__name {
    font-weight: 700; font-size: 30px; color: var(--text-light); letter-spacing: .5px;
  }
  .divider { width: 1px; height: 180px; background: var(--divider); }
  .contact { padding-left: 36px; color: var(--text-soft); }
  .contact__name { font-weight: 700; font-size: 24px; color: var(--text-light); }
  .contact__role { font-size: 15px; margin-top: 2px; }
  .contact__address { font-size: 15px; line-height: 1.35; margin-top: 18px; }
  .contact__list { list-style: none; margin-top: 14px; font-size: 15px; line-height: 1.5; }
  .contact__list li { display: flex; align-items: center; gap: 10px; }
  .contact__list svg { width: 13px; height: 13px; flex: none; }
  /* Back */
  .card--back { display: flex; align-items: center; justify-content: center; gap: 18px; }
  .card--back .brand__mark { width: 24px; height: 24px; background: var(--emboss); box-shadow: 0 1px 0 var(--emboss-edge); }
  .card--back .brand__name {
    font-size: 44px; color: var(--emboss);
  }
</style>
</head>
<body>
<main class="sheet">
  <section class="card card--front" aria-label="Business card front">
    <div class="brand">
      <span class="brand__mark"></span>
      <span class="brand__name">Korvex Systems</span>
    </div>
    <div class="divider"></div>
    <div class="contact">
      <p class="contact__name">Daniel Reyes</p>
      <p class="contact__role">Founder &amp; CEO</p>
      <p class="contact__address">41 Harbor Street Suite 120<br>Sample City, Country</p>
      <ul class="contact__list">
        <li>
          <svg viewBox="0 0 16 16" aria-hidden="true"><path fill="#fff" d="M4 1l2.5 3-1.5 2c1 2 3 4 5 5l2-1.5 3 2.5-1.5 2C7 15 1 9 2 2.5z"/></svg>
          +1 555.010.0000
        </li>
        <li>
          <svg viewBox="0 0 16 16" aria-hidden="true"><rect x="1" y="3" width="14" height="10" fill="#fff"/><path d="M1 3l7 6 7-6" stroke="#2a2b2c" stroke-width="1.4" fill="none"/></svg>
          info@korvexsystems.example
        </li>
        <li>
          <svg viewBox="0 0 16 16" aria-hidden="true" fill="none" stroke="#fff" stroke-width="1.2"><circle cx="8" cy="8" r="6.5"/><ellipse cx="8" cy="8" rx="3" ry="6.5"/><path d="M1.5 8h13M2.5 4.8h11M2.5 11.2h11"/></svg>
          www.korvexsystems.example
        </li>
      </ul>
    </div>
  </section>

  <section class="card card--back" aria-label="Business card back">
    <span class="brand__mark"></span>
    <span class="brand__name">Korvex Systems</span>
  </section>
</main>
</body>
</html>
```